website design for Company KMV

Our company name KMV(the civic canvas limited), need design a website. It is a website that focuses on promoting art design in the world.
We will provide the existing logo design, the new website and logo should be matched to each other. The website has to include pages "Home" "Contact" "Service" and So on at least 6-8 pages. The site is mainly for publicity and promotion. We will have an existing domain and hosting.
Updates

We prefer the original design, thanks.

Target Market(s)

large public art

Industry/Entity Type

Architecture and design, large public art and sculpture manufacturer

Coding

Coded - Design and coding required

Number of Pages Required

5+ page

Requirements
Must have
• 1. the overall color has to match our logo color 2. Do not need to do any change on our logo including the color 3. Here is a similar style of the home page we like, it can be similar but must not same. Pls check the below link. https://www.darveno.example/en-us/

```html
<!DOCTYPE html>
<html lang="en">
<head>
<meta charset="utf-8">
<title>KMV — The Civic Canvas</title>
<link href="https://fonts.googleapis.com/css2?family=Oswald:wght@400;500;600&family=Poppins:wght@300;400;600&display=swap" rel="stylesheet">
<style>
  :root{
    --ink:#2f2f2f;
    --charcoal:#3a3a3a;
    --muted:#555;
    --field:#efefef;
    --rule:#cfcfcf;
    --white:#fff;
  }
  *{box-sizing:border-box;margin:0;padding:0}
  html,body{width:1200px;height:4721px;overflow:hidden;background:var(--white)}
  body{position:relative;font-family:'Poppins',sans-serif;color:var(--ink)}
  .abs{position:absolute}
  .cond{font-family:'Oswald',sans-serif;text-transform:uppercase}

  /* header */
  .site-header{left:0;top:0;width:1200px;height:86px;background:var(--white)}
  .brand{left:88px;top:22px;display:flex;align-items:center;gap:10px;color:var(--ink);font-family:'Poppins',sans-serif;font-weight:400;white-space:nowrap}
  .brand .mark{font-size:34px;letter-spacing:1px}
  .brand .name{font-size:17px;line-height:18px;letter-spacing:2px;text-transform:uppercase}
  .main-nav{left:563px;top:34px;display:flex;gap:24px;font-size:13px}
  .main-nav a{color:var(--ink);text-decoration:none}
  .nav-cta{left:916px;top:22px;width:109px;height:40px;background:#575757;color:var(--white);font-size:14px;display:flex;align-items:center;justify-content:center}
  .nav-icons{left:1046px;top:30px}

  /* hero */
  .hero{left:0;top:86px;width:1200px;height:716px;background:linear-gradient(180deg,#a89f94 0%,#7b7670 40%,#5c5a58 65%,#8d8a86 100%)}
  .hero-arrow{top:410px;width:44px;height:66px;background:rgba(40,40,40,.6)}
  .hero-kicker{left:0;width:1200px;top:368px;text-align:center;color:var(--white);font-size:22px}
  .hero-title{left:0;width:1200px;top:385px;text-align:center;color:var(--white);font-size:128px;font-weight:500;line-height:150px}
  .hero-link{left:0;width:1200px;top:706px;text-align:center;color:var(--white);font-size:21px;text-decoration:underline;text-underline-offset:4px}
  .hero-thumb{left:947px;top:720px;width:253px;height:157px;background:var(--white);padding:7px}
  .hero-thumb div{width:100%;height:100%;background:linear-gradient(180deg,#6d9ad6 0%,#9ab7dc 55%,#b58b6a 100%)}

  /* section heading */
  .kicker{display:flex;align-items:center;gap:10px;font-size:28px;color:var(--ink)}
  .kicker::before{content:"";width:67px;height:2px;background:var(--ink)}
  .big{font-size:68px;font-weight:500;line-height:78px;color:var(--ink)}
  .copy{width:520px;font-size:18px;line-height:31px;color:var(--muted);font-weight:300}
  .text-link{font-size:19px;text-decoration:underline;text-underline-offset:4px;color:var(--ink)}

  /* cards */
  .photo{overflow:hidden}
  .caption{color:var(--white);font-size:27px;font-weight:500}

  /* form */
  .label{font-size:11px;font-weight:600;text-transform:uppercase}
  .field{height:40px;background:var(--field);font-size:13px;color:#8a8a8a;padding:11px 18px}
  .submit{left:489px;top:4102px;width:553px;height:55px;background:var(--ink);color:var(--white);font-weight:600;font-size:16px;display:flex;align-items:center;justify-content:center}

  /* footer */
  .site-footer{left:0;top:4265px;width:1200px;height:456px;background:var(--charcoal);color:var(--white)}
  .foot-nav{left:0;width:1200px;top:205px;display:flex;justify-content:center;gap:22px;font-size:14px}
  .social{top:250px;left:527px;display:flex;gap:7px}
  .social span{width:33px;height:33px;background:#555}
  .chat{left:1079px;top:187px;width:53px;height:52px;background:var(--white)}
  .copyright{left:0;width:1200px;top:423px;text-align:center;font-size:11px}
</style>
</head>
<body>

<header class="site-header abs">
  <div class="brand abs"><span class="mark">KMV</span><span class="name">The<br>Civic Canvas</span></div>
  <nav class="main-nav abs cond">
    <a href="#">Home</a><a href="#">Service</a><a href="#">Products</a><a href="#">Lifestyle</a><a href="#">Contract</a>
  </nav>
  <div class="nav-cta abs cond">Contact us</div>
  <svg class="nav-icons abs" width="60" height="26" viewBox="0 0 60 26" fill="none" stroke="#333" stroke-width="1.8">
    <circle cx="10" cy="11" r="7"/><line x1="15" y1="16" x2="20" y2="21"/>
    <path d="M34 6h4l3 11h11l3-8H39"/><circle cx="43" cy="21" r="1.5"/><circle cx="51" cy="21" r="1.5"/>
    <circle cx="56" cy="5" r="4" fill="#333" stroke="none"/>
  </svg>
</header>

<section class="hero abs" role="img" aria-label="Large twisted metal sculpture in front of a classical palace facade">
</section>
<div class="hero-arrow abs" style="left:0"><svg width="44" height="66"><path d="M25 28l-6 5 6 5" stroke="#fff" stroke-width="2" fill="none"/></svg></div>
<div class="hero-arrow abs" style="left:1156px"><svg width="44" height="66"><path d="M19 28l6 5-6 5" stroke="#fff" stroke-width="2" fill="none"/></svg></div>
<div class="hero-kicker abs cond">KMV The Civic Canvas</div>
<h1 class="hero-title abs cond">Sculpture</h1>
<div class="hero-link abs cond">Discover</div>
<div class="hero-thumb abs"><div role="img" aria-label="Sculpture on a city square under blue sky"></div></div>

<!-- new collection -->
<div class="abs" style="left:155px;top:980px">
  <div class="kicker cond">New</div>
  <div class="big cond">Collection</div>
</div>
<p class="copy abs" style="left:508px;top:939px">Lorem Ipsum is simply dummy text of the printing and typesetting industry. Lorem Ipsum has been the industry's standard dummy text ever since the 1500s, when an unknown printer took a galley of type and scrambled it to make a type specimen book. It has survived not only five centuries, but also the leap into electronic typesetting, remaining essentially unchanged.</p>
<div class="text-link abs cond" style="left:508px;top:1183px">Discover</div>

<div class="photo abs" style="left:88px;top:1328px;width:787px;height:479px;background:linear-gradient(180deg,#8c9bb0 0%,#b8bcc0 45%,#5b6460 75%,#4a4d4c 100%)" role="img" aria-label="Twisting steel sculpture beside a glass pavilion"></div>
<div class="caption abs cond" style="left:141px;top:1734px">Sculpture Diagnostics</div>
<div class="text-link abs cond" style="left:750px;top:1741px;color:#fff;font-size:17px">Discover</div>
<div class="photo abs" style="left:894px;top:1328px;width:306px;height:479px;background:linear-gradient(180deg,#9fa0a0 0%,#8a5a3c 45%,#6e4a35 80%,#7a7a78 100%)" role="img" aria-label="Rust-coloured abstract sculpture in an atrium"></div>

<!-- about -->
<div class="abs" style="left:155px;top:1966px">
  <div class="kicker cond">About</div>
  <div class="big cond">Sculpture</div>
</div>
<p class="copy abs" style="left:508px;top:1925px">Lorem Ipsum is simply dummy text of the printing and typesetting industry. Lorem Ipsum has been the industry's standard dummy text ever since the 1500s, when an unknown printer took a galley of type and scrambled it to make a type specimen book. It has survived not only five centuries, but also the leap into electronic typesetting, remaining essentially unchanged.</p>
<div class="text-link abs cond" style="left:508px;top:2169px">Discover</div>

<section class="abs" style="left:0;top:2328px;width:1200px;height:578px;background:linear-gradient(180deg,#5d5d5d 0%,#8a8a8a 50%,#a9a7a3 100%)" role="img" aria-label="Video still of a fluted metal wing sculpture before a library facade"></section>
<svg class="abs" style="left:537px;top:2553px" width="126" height="126" viewBox="0 0 126 126">
  <circle cx="63" cy="63" r="63" fill="rgba(40,40,40,.75)"/><path d="M56 52l17 11-17 11z" fill="#fff"/>
</svg>

<!-- portfolio -->
<div class="abs" style="left:155px;top:2988px">
  <div class="kicker cond">Public</div>
  <div class="big cond">Portfolio</div>
</div>
<div class="abs" style="left:447px;top:3044px;width:503px;height:1px;background:var(--rule)"></div>
<svg class="abs" style="left:978px;top:3022px" width="63" height="42" viewBox="0 0 63 42">
  <rect width="30" height="42" fill="#eee"/><rect x="33" width="30" height="42" fill="#eee"/>
  <path d="M17 16l-5 5 5 5M46 16l5 5-5 5" stroke="#333" stroke-width="1.6" fill="none"/>
</svg>

<div class="photo abs" style="left:89px;top:3168px;width:336px;height:474px;background:linear-gradient(180deg,#9a9a9a 0%,#6a6a6a 50%,#8b6a45 70%,#3d3d3d 100%)" role="img" aria-label="Modern building with a ribbed facade at dusk"></div>
<div class="photo abs" style="left:432px;top:3168px;width:336px;height:474px;background:linear-gradient(180deg,#6f8094 0%,#7a6a55 50%,#4e5a3a 80%,#8a8a84 100%)" role="img" aria-label="Wire mesh shell sculpture in a park"></div>
<div class="photo abs" style="left:774px;top:3168px;width:336px;height:474px;background:linear-gradient(180deg,#c9c9c9 0%,#8b8b8b 55%,#5e5e5e 100%)" role="img" aria-label="Classical marble statue in a gallery"></div>
<div class="caption abs cond" style="left:89px;width:336px;top:3581px;text-align:center;font-size:23px">Architecture and Design</div>
<div class="caption abs cond" style="left:432px;width:336px;top:3581px;text-align:center;font-size:23px">Large Public Art</div>
<div class="caption abs cond" style="left:774px;width:336px;top:3581px;text-align:center;font-size:23px">Sculpture Manufacturer</div>

<!-- contact -->
<div class="abs" style="left:155px;top:3903px">
  <div class="kicker cond">Form</div>
  <div class="big cond">Contact</div>
</div>
<form>
  <div class="label abs" style="left:489px;top:3752px">First name*</div>
  <div class="label abs" style="left:769px;top:3752px">Last name*</div>
  <div class="field abs" style="left:489px;top:3774px;width:271px">Enter first name</div>
  <div class="field abs" style="left:769px;top:3774px;width:273px">Enter first name</div>
  <div class="label abs" style="left:489px;top:3829px">Email*</div>
  <div class="label abs" style="left:769px;top:3829px">Mobile*</div>
  <div class="field abs" style="left:489px;top:3850px;width:271px">Enter email address</div>
  <div class="field abs" style="left:769px;top:3850px;width:273px">Enter mobile number</div>
  <div class="label abs" style="left:489px;top:3905px">Message*</div>
  <div class="field abs" style="left:489px;top:3926px;width:553px;height:149px">Type your text</div>
  <div class="submit abs">SUBMIT NOW
    <svg class="abs" style="left:509px;top:19px" width="20" height="18" viewBox="0 0 20 18"><path d="M1 8L19 1l-4 16-5-6z" fill="#fff"/></svg>
  </div>
</form>

<footer class="site-footer abs">
  <div class="brand abs" style="left:437px;top:122px;color:#fff"><span class="mark">KMV</span><span class="name">The<br>Civic Canvas</span></div>
  <nav class="foot-nav abs cond"><span>Home</span><span>Service</span><span>Products</span><span>Lifestyle</span><span>Contract</span><span>Contact us</span></nav>
  <div class="social abs"><span></span><span></span><span></span><span></span></div>
  <div class="chat abs"><svg width="53" height="52"><circle cx="27" cy="26" r="10" fill="none" stroke="#333" stroke-width="2"/><path d="M20 33l-3 5 6-2" fill="#333"/></svg></div>
  <div class="copyright abs">© COPYRIGHT 2021 THE CIVIC CANVAS ALL RIGHTS RESERVED</div>
</footer>

</body>
</html>
```